Talvoro Equity LLC

Need Professional Business cards for New Investment Fund

Target Market(s)

High Quality investors

Industry/Entity Type

Financial

Contact Information for Business Card

Phone Number +1 555 284 6190
Name Milan Dorovsky
Title Fund Manager
email md@FundTalvoro.com
Website www.FundTalvoro.com

Colors

Designer to choose colors to be used in the design.

Requirements
Must have
• Must have our Logo and all of the above. Must be made so lettering and loge can be raised

```html
<!DOCTYPE html>
<html lang="en">
<head>
<meta charset="utf-8">
<title>Talvoro Equity – Business Card</title>
<link href="https://fonts.googleapis.com/css2?family=Roboto:wght@400;500;700&display=swap" rel="stylesheet">
<style>
  :root {
    --backdrop: #e4e4e4;
    --card-white: #ffffff;
    --brand-green: #22ea08;
    --ink-grey: #4a4f48;
    --divider: #6a6d68;
    --back-top: #535c51;
    --back-bottom: #434c41;
    --back-text: #ffffff;
  }
  * { margin: 0; padding: 0; box-sizing: border-box; }
  html, body { width: 1200px; height: 1200px; overflow: hidden; }
  body {
    background: var(--backdrop);
    font-family: "Roboto", Arial, sans-serif;
    position: relative;
  }
  .card {
    position: absolute;
    left: 200px;
    width: 800px;
    height: 456px;
    box-shadow: 0 18px 30px rgba(0,0,0,0.25);
  }
  .card-front { top: 87px; background: var(--card-white); }
  .card-back {
    top: 656px;
    background: linear-gradient(to bottom, var(--back-top), var(--back-bottom));
  }
  .front-band {
    position: absolute; left: 0; right: 0; bottom: 0;
    height: 8px; background: var(--brand-green);
  }
  .brand-name {
    position: absolute;
    color: var(--brand-green);
    font-weight: 700;
    white-space: nowrap;
    transform: translate(-50%, -50%);
    letter-spacing: 0.5px;
  }
  .card-front .brand-name { left: 242px; top: 228px; font-size: 42px; }
  .card-back .brand-name { left: 400px; top: 250px; font-size: 68px; }
  .divider {
    position: absolute; left: 359px; top: 143px;
    width: 2px; height: 170px; background: var(--divider);
  }
  .contact-block { position: absolute; left: 399px; top: 155px; }
  .person-name {
    color: var(--brand-green); font-weight: 700; font-size: 27px; line-height: 32px;
  }
  .person-title {
    color: var(--ink-grey); font-weight: 500; font-size: 18px; line-height: 22px;
  }
  .contact-list { list-style: none; margin-top: 17px; }
  .contact-list li {
    display: flex; align-items: center;
    color: var(--ink-grey); font-size: 18px; line-height: 23px;
  }
  .contact-list svg { width: 15px; height: 15px; margin-right: 11px; flex: none; }
  .back-url {
    position: absolute; left: 0; right: 0; top: 404px;
    text-align: center; color: var(--back-text);
    font-size: 18px; letter-spacing: 3.6px;
  }
</style>
</head>
<body>
  <section class="card card-front">
    <div class="brand-name">Talvoro</div>
    <div class="divider"></div>
    <div class="contact-block">
      <div class="person-name">Milan Dorovsky</div>
      <div class="person-title">Fund Manager</div>
      <ul class="contact-list">
        <li>
          <svg viewBox="0 0 16 16" aria-hidden="true"><path fill="#22ea08" d="M3.5 1.5l2.5 0 1 3.5-1.6 1.2c.8 1.8 2.2 3.2 4 4l1.2-1.6 3.4 1v2.6c0 .9-.7 1.5-1.6 1.4C6.5 13 3 9.5 2.2 3.1 2.1 2.2 2.7 1.5 3.5 1.5z"/></svg>
          +1 555 284 6190
        </li>
        <li>
          <svg viewBox="0 0 16 16" aria-hidden="true"><rect x="1.5" y="4" width="13" height="9" fill="#22ea08"/><path d="M1.5 4.5L8 9l6.5-4.5" fill="none" stroke="#fff" stroke-width="1.2"/></svg>
          md@FundTalvoro.com
        </li>
        <li>
          <svg viewBox="0 0 16 16" aria-hidden="true"><circle cx="8" cy="8" r="6.5" fill="#22ea08"/><path d="M1.5 8h13M8 1.5c-2.5 3-2.5 10 0 13M8 1.5c2.5 3 2.5 10 0 13" fill="none" stroke="#fff" stroke-width="1"/></svg>
          www.FundTalvoro.com
        </li>
      </ul>
    </div>
    <div class="front-band"></div>
  </section>

  <section class="card card-back">
    <div class="brand-name">Talvoro</div>
    <div class="back-url">www.FundTalvoro.com</div>
  </section>
</body>
</html>
```